Flyer-Design für Anbieter von hochwertigem Futter für Kaninchen
Zielgruppe
Wir bieten hochwertiges Futter (Hauptfutter wie Heu aus eigener Herstellung aber auch Zusatzfutter) für Kaninchen.
Unsere Zielgruppe sind laut Auswertung unsers Online-Shops hauptsächlich weibliche Kunden (82%) und im Durchschnitt 40 Jahre alt.
Aufgabenstellung
Allgemeines:
- Flyer soll als Werbemedium gestaltet werden
- Design im Querformat DinA5
Inhalte:
- Logo Grasbündel.de
- www. grasbündel.de
- Kunden bewerten mit 'sehr gut'
- Familienbetrieb seit über 100 Jahren
- Geprüftes Qualitätsheu aus der Eifel
- frischer, aromatischer Heuduft von naturbelassenen, grünen Eifelwiesen
- Heu, Stroh und viele weitere Produkte im Shop
- Ökologische Papier-Verpackung
- Schneller und kostengünstiger Versand
Zusatzinfos:
- Die Datei normalheupng.png kann als Logo verwendet werden
- Als Idee könnte evt. auch ein Bild 89328394.jpg (Eifellandschaft Heuernte) in irgendweiner Form integriert werden.
- Folgende Bilddateien wurden über Bildaro gekauft:
- Es können bei Bedarf auch Kosten für weitere Bilder erworben werden

```html
<!DOCTYPE html>
<html lang="de">
<head>
<meta charset="utf-8">
<title>Grasbündel – Flyer</title>
<link rel="stylesheet" href="https://fonts.googleapis.com/css2?family=Signika:wght@400;600;700&family=Great+Vibes&display=swap">
<style>
  :root {
    --band-blue: #0f6590;
    --text-blue: #1b6a95;
    --text-olive: #4a4528;
    --footer-bg: #f3f6e6;
    --white: #ffffff;
    --ink: #222222;
    --field-top: #d9d2a6;
    --field-mid: #a9a64a;
    --field-low: #b59a3c;
    --hay-light: #c9c3b4;
    --hay-dark: #6f6a5c;
  }
  * { box-sizing: border-box; margin: 0; padding: 0; }
  html, body { width: 1200px; height: 846px; overflow: hidden; background: var(--white); }
  body { font-family: "Signika", sans-serif; }
  .flyer { position: relative; width: 1200px; height: 846px; overflow: hidden; background: var(--white); }

  .hero-photo {
    position: absolute; left: 0; top: 0; width: 1200px; height: 390px;
    background: linear-gradient(180deg, var(--field-top) 0%, #9ea25a 35%, var(--field-mid) 60%, var(--field-low) 100%);
  }
  .headline {
    position: absolute; left: 22px; top: 78px; width: 420px;
    text-align: center; color: var(--white);
    font-weight: 700; font-size: 70px; line-height: 82px; letter-spacing: 0.5px;
  }
  .tagline {
    position: absolute; left: 780px; top: 95px; width: 420px;
    font-family: "Great Vibes", cursive; color: var(--white);
    font-size: 52px; line-height: 82px; text-align: center;
  }
  .tagline .von { display: block; text-align: left; padding-left: 0; }

  .info-band {
    position: absolute; left: 0; top: 389px; width: 1200px; height: 72px;
    background: var(--band-blue); color: var(--white);
  }
  .rating { position: absolute; left: 30px; top: 22px; font-size: 22px; }
  .web { position: absolute; left: 805px; top: 16px; font-size: 29px; letter-spacing: 0.5px; }

  .hay-panel {
    position: absolute; left: 446px; top: 82px; width: 278px; height: 410px;
    border-radius: 60px 60px 90px 90px;
    background: linear-gradient(135deg, var(--hay-light), var(--hay-dark) 55%, var(--hay-light));
  }
  .brand {
    position: absolute; left: 430px; top: 506px; width: 310px;
    text-align: center; color: var(--ink); font-weight: 700; font-size: 48px;
  }

  .photo-strip { position: absolute; top: 461px; height: 152px; overflow: hidden; display: flex; }
  .photo-strip.left { left: 0; width: 382px; border-bottom-right-radius: 18px; }
  .photo-strip.right { left: 794px; width: 406px; border-bottom-left-radius: 18px; }
  .photo { height: 100%; }
  .photo.rabbits { width: 210px; background: linear-gradient(180deg, #f4f4f4 60%, #7fb23a 100%); }
  .photo.branches { width: 172px; background: linear-gradient(135deg, #5a4a3e, #9a6a4a 50%, #4a3c32); }
  .photo.hay-bag { width: 194px; background: linear-gradient(180deg, #6fa33a, #b28c5e 45%, #6f9a35); }
  .photo.rabbit-carrots { width: 212px; background: linear-gradient(160deg, #e8d8c0, #d2a070 55%, #e07a2a); }

  .since { position: absolute; left: 0; top: 630px; width: 1200px; text-align: center; color: var(--text-blue); font-size: 23px; }
  .features {
    position: absolute; left: 64px; top: 682px; width: 1100px;
    display: grid; grid-template-columns: 595px 500px; row-gap: 8px;
    list-style: none; color: var(--text-olive); font-size: 24px; line-height: 30px;
  }
  .features li::before { content: "·"; display: inline-block; width: 20px; }

  .owner-bar {
    position: absolute; left: 0; top: 786px; width: 1200px; height: 60px;
    background: var(--footer-bg); color: var(--text-blue);
    font-size: 19px; text-align: center; line-height: 60px;
  }
</style>
</head>
<body>
<main class="flyer">
  <div class="hero-photo" role="img" aria-label="Foto: hügelige Eifellandschaft mit Heuballen auf gemähten Wiesen"></div>

  <h1 class="headline">Frischer,<br>aromatischer<br>Heuduft</h1>
  <p class="tagline"><span class="von">von</span>naturbelassenen,<br>grünen Eifelwiesen</p>

  <div class="info-band">
    <span class="rating">Kunden bewerten mit ‚sehr gut‘</span>
    <span class="web">www.grasbündel.de</span>
  </div>

  <div class="hay-panel" role="img" aria-label="Foto: Nahaufnahme von frischem Heu"></div>
  <div class="brand">Grasbündel</div>

  <div class="photo-strip left">
    <div class="photo rabbits" role="img" aria-label="Foto: drei Kaninchen im Gras"></div>
    <div class="photo branches" role="img" aria-label="Foto: Knabberäste"></div>
  </div>
  <div class="photo-strip right">
    <div class="photo hay-bag" role="img" aria-label="Foto: Heu in Papiertüte auf Wiese"></div>
    <div class="photo rabbit-carrots" role="img" aria-label="Foto: Kaninchen mit Karotten und Gemüse"></div>
  </div>

  <p class="since">Familienbetrieb seit über 100 Jahren</p>
  <ul class="features">
    <li>Heu, Stroh und viele weitere Produkte im Shop</li>
    <li>Schneller und kostengünstiger Versand</li>
    <li>Ökologische Papier-Verpackung</li>
    <li>Geprüftes Qualitätsheu aus der Eifel</li>
  </ul>

  <footer class="owner-bar">Inhaber: K. Lorenz, Lindenweg 12, 54321 Feldhausen, mail@grasbuendel.de</footer>
</main>
</body>
</html>
```